Web Site for Strategy and Technology Consulting Company

We are looking for a website design that engages potential customers to understand our services and contact us. In this contest, we are looking for a homepage design, but the winning designer will be favored for the design of some of the more complicated interior pages of the site. An additional contest (or contests) for these pages will be added soon.

PLATROM AND RESPONSIVE DESIGN
The site will be implemented in WordPress using the Elementor page builder.
We are looking for a design that will look good on phones are well as laptop browsers.

UPLOADED FILES INCLUDE:
1a A wireframe of the homepage we are looking for. The Uploaded PDF also includes a draft of the text proposed for the homepage. Designers are free to go beyond the wireframe, but all elements of the wireframe should be included.
1b A Word document with the draft text of the homepage.
2a-d The Corvalin logo. Two versions are included – a dark version which works well against a light background, and a light version which works well against a dark background.
3 The Corvalin color palette with HEX and RGB values. Designers are not limited to this palette, but colors should be complementary.
4 A draft of the homepage menu
5 Service sheets with information on the services we provide

MORE ABOUT CORVALIN
Corvalin is a consulting company focused on transforming businesses through software. Our tagline, “Transformation Delivered,” recognizes the gap business often have between business transformation and the software they end up with. By listening to our customers and understanding their vision and where they are, we help get our customers where they want to go.

We increase our capability by working with many consultants and partners, allowing us to provide our customers with the best people and the software that best suits them.

Industry/Entity Type

Consulting

Number of Pages Required

1 page

Font styles to use
Sans Serif

Requirements
Must have
• the content represented on the wireframe uploaded
Nice to have
• interactive features, such as roll-over icons that reveal additional information

```html
<!DOCTYPE html>
<html lang="en">
<head>
<meta charset="utf-8">
<title>Corvalin — Transformation Delivered</title>
<link href="https://fonts.googleapis.com/css2?family=Poppins:wght@600;700;800&family=League+Spartan:wght@400;500;600;700&display=swap" rel="stylesheet">
<style>
:root{
  --blue:#2b62a4;
  --sky:#bcd9f1;
  --sky-2:#8eaee8;
  --yellow:#f5c518;
  --ink:#1d1d1f;
  --text:#3b3b3b;
  --muted:#9a9a9a;
  --white:#ffffff;
  --footer:#2b2b2b;
  --olive:#8a9a3c;
}
*{box-sizing:border-box;margin:0;padding:0}
html,body{width:1200px;height:4485px;overflow:hidden}
body{font-family:"League Spartan",Arial,sans-serif;color:var(--text);background:var(--white);position:relative}
h1,h2,h3{font-family:"Poppins",Arial,sans-serif;color:var(--ink)}
.sq{position:absolute}
.pixel-deco{position:absolute;background:linear-gradient(135deg,rgba(142,174,232,.55),rgba(43,98,164,.45) 55%,rgba(245,197,24,.45));z-index:2}
/* hero */
.hero{position:absolute;left:0;top:0;width:1200px;height:750px}
.sidebar{position:absolute;left:0;top:0;width:244px;height:750px;background:var(--white)}
.logo{position:absolute;left:28px;top:36px;font-weight:500;font-size:40px;color:#5a6f8f;letter-spacing:.5px}
.nav a{position:absolute;left:0;width:244px;text-align:center;font-size:20px;color:var(--ink);text-decoration:none}
.btn-contact{position:absolute;left:37px;top:655px;width:170px;height:45px;background:var(--blue);color:#fff;font-size:12px;font-weight:600;display:flex;align-items:center;justify-content:center;border:2px solid #9cc0e8;text-decoration:none}
.hero-photo{position:absolute;left:244px;top:0;width:956px;height:750px;background:linear-gradient(90deg,#2f2f2f 0%,#3a3a38 45%,#6b6e62 75%,#8a8c80 100%)}
.hero-title{position:absolute;left:320px;top:82px;font-weight:800;font-size:56px;line-height:64px;color:#fff}
.hero-copy{position:absolute;left:320px;top:226px;width:455px;font-size:14.5px;line-height:22px;color:#eee}
.hero-list{position:absolute;left:320px;top:372px;width:430px;list-style:none;font-size:14.5px;line-height:22px;color:#eee}
.hero-list li{position:relative;padding-left:30px;margin-bottom:13px}
.hero-list li::before{content:"";position:absolute;left:0;top:6px;width:10px;height:10px;background:var(--blue);border:2px solid #7fa4d6}
.hero-tag{position:absolute;left:320px;top:600px;font-size:19px;color:var(--yellow)}
/* services */
.sec-title{position:absolute;left:0;width:1200px;text-align:center;font-weight:700;font-size:40px;line-height:50px}
.sec-copy{position:absolute;left:195px;width:810px;text-align:center;font-size:13.5px;line-height:20px}
.card{position:absolute;width:462px;height:140px;background:#fff;box-shadow:0 4px 22px rgba(0,0,0,.08);display:flex;align-items:center;padding-left:50px}
.card .icon{width:46px;height:46px;background:linear-gradient(135deg,#fde68a,#f5c518);border-radius:6px;flex:none}
.card .bar{width:1px;height:26px;background:#bbb;margin:0 28px 0 30px}
.card h3{font-size:14.5px;font-weight:700;margin-bottom:6px}
.card p{font-size:13px;line-height:19px;width:240px}
.link-cta{position:absolute;left:0;width:1200px;text-align:center;font-size:18px;line-height:30px;font-weight:600;color:var(--blue)}
/* people */
.people{position:absolute;left:0;top:1735px;width:1200px;height:750px;background:var(--sky);overflow:hidden}
.tile{position:absolute}
.pink{background:linear-gradient(160deg,#f7b7c7,#ee9cb3)}
.teal{background:linear-gradient(160deg,#7fd6d4,#5ec6c7)}
.grey{background:linear-gradient(160deg,#e6e6e6,#cfcfcf)}
.blue-t{background:linear-gradient(160deg,#7fb0d8,#5e97c9)}
.people h2{position:absolute;left:581px;top:120px;font-size:38px;font-weight:700}
.people .copy{position:absolute;left:581px;top:198px;width:480px;font-size:13.5px;line-height:21px}
.people .box{position:absolute;left:581px;width:486px;background:var(--blue);color:#fff;font-size:13px;font-weight:600;line-height:22px;padding:0 36px;display:flex;align-items:center}
.people .strong{position:absolute;left:581px;top:572px;width:500px;font-size:14px;line-height:27px;font-weight:600;color:var(--ink)}
/* testimonials */
.testi-col{position:absolute;top:2660px;width:225px;display:flex;flex-direction:column;gap:20px}
.t-card{background:#fff;box-shadow:0 4px 22px rgba(0,0,0,.08);padding:22px 26px}
.t-head{display:flex;align-items:center;gap:10px;margin-bottom:20px}
.avatar{width:30px;height:30px;border-radius:50%;background:linear-gradient(#d8d8d8,#b5b5b5);flex:none}
.t-head b{display:block;font-family:"Poppins",sans-serif;font-size:12px;color:var(--ink)}
.t-head span{font-size:8.5px;color:var(--muted)}
.t-card p{font-size:9.5px;line-height:15px;color:#444}
.stars{margin-top:20px;color:var(--yellow);font-size:13px;letter-spacing:7px}
/* tech */
.tech{position:absolute;left:0;top:3335px;width:1200px;height:665px;background:var(--blue);overflow:hidden}
.tech h2{position:absolute;left:125px;top:232px;font-size:40px;color:#fff;font-weight:700}
.arrow-btn{position:absolute;top:320px;width:70px;height:46px;border-radius:23px;background:var(--olive)}
.shot{position:absolute;top:100px;width:340px;height:400px}
.caption{position:absolute;top:530px;font-size:20px;font-weight:600;color:var(--yellow)}
/* footer */
.footer{position:absolute;left:0;top:4000px;width:1200px;height:485px;background:var(--footer);color:#eee}
.f-logo{position:absolute;left:125px;top:90px;font-size:58px;font-weight:500;color:#fff}
.f-item{position:absolute;left:125px;display:flex;align-items:center;gap:18px;font-size:12.5px;line-height:19px}
.f-icon{width:52px;height:52px;border-radius:50%;border:1.5px solid #ddd;display:flex;align-items:center;justify-content:center;flex:none}
.f-col{position:absolute;top:140px}
.f-col h4{font-family:"Poppins",sans-serif;font-size:18px;color:#fff;margin-bottom:26px}
.f-col a{display:block;color:#eee;text-decoration:none;font-size:14px;margin-bottom:31px}
.copy-r{position:absolute;left:890px;top:318px;font-size:12px}
.social{position:absolute;top:372px;width:26px;height:26px;border-radius:50%;background:var(--yellow)}
</style>
</head>
<body>

<header class="hero">
  <div class="hero-photo" role="img" aria-label="Photo of a smiling consultant with glasses, hands clasped, on a dark background"></div>
  <aside class="sidebar">
    <div class="logo">Corvalin</div>
    <nav class="nav">
      <a href="#" style="top:238px">About Us</a>
      <a href="#" style="top:316px">Services</a>
      <a href="#" style="top:394px">Insights</a>
      <a href="#" style="top:472px">Join Us</a>
    </nav>
    <a class="btn-contact" href="#">Contact Us</a>
  </aside>
  <h1 class="hero-title">Transformation<br>Delivered</h1>
  <p class="hero-copy">We Do More For Our Customers Than Implement Software. We Listen. We Work To Understand Where They Are In Their Transformation Journey And Where They Want To Go. We Partner With Them To Clear The Roadblocks That Stand In Their Way, Ensuring They Reach Their Destination. At Corvalin, We:</p>
  <ul class="hero-list">
    <li>Focus On Business Value, With An Emphasis On Delivering Value Quickly.</li>
    <li>Meet Our Customers Where They Are Without Backing Them Up To The Beginning Of Their Journey.</li>
    <li>Provide A Wide Range Of Services, From Strategy To Product Support.</li>
    <li>Commit To Our Customer's Long-Term Success.</li>
  </ul>
  <p class="hero-tag">Corvalin Is Business Transformation, Delivered.</p>
</header>
<div class="pixel-deco" style="left:920px;top:640px;width:280px;height:150px" role="img" aria-label="Decorative cluster of pixel squares"></div>

<section class="services">
  <h2 class="sec-title" style="top:840px">Transformation<br>Supported By Technology</h2>
  <p class="sec-copy" style="top:966px">During Our Early Years, Corvalin Focused Only On Business Transformation. We Came To Realize That Successful Transformation Often Depended On Quality Software Implementations, And Often More Than One. Now We Focus On Five Things, The Five Things Most Businesses Need To Reach Their Goals.</p>
  <div class="sq" style="left:0;top:1005px;width:12px;height:12px;background:var(--sky-2)"></div>

  <div class="card" style="left:125px;top:1072px"><div class="icon" role="img" aria-label="Business transformation icon"></div><div class="bar"></div><div><h3>Business Transformation</h3><p>Define And Execute Your Strategy</p></div></div>
  <div class="card" style="left:610px;top:1072px"><div class="icon" role="img" aria-label="ERP implementation gear icon"></div><div class="bar"></div><div><h3>ERP Implementations</h3><p>Assess, Upgrade, And Implement ERP Solutions To Meet Your Needs</p></div></div>
  <div class="card" style="left:125px;top:1233px"><div class="icon" role="img" aria-label="CRM implementation icon"></div><div class="bar"></div><div><h3>CRM Implementations</h3><p>Define And Execute Your Strategy</p></div></div>
  <div class="card" style="left:610px;top:1233px"><div class="icon" role="img" aria-label="BI and data dashboard icon"></div><div class="bar"></div><div><h3>BI And Data</h3><p>Discover, Connect, And Trust Your Data.</p></div></div>
  <div class="card" style="left:367px;top:1395px"><div class="icon" role="img" aria-label="Team of people icon"></div><div class="bar"></div><div><h3>Building The Right Team<br>Of People</h3><p>Hire Resources For Your Transformation Journey</p></div></div>

  <div class="pixel-deco" style="left:0;top:1452px;width:86px;height:126px" role="img" aria-label="Decorative cluster of pixel squares"></div>
  <div class="sq" style="left:1083px;top:1505px;width:10px;height:10px;background:var(--yellow)"></div>

  <p class="link-cta" style="top:1584px">Find Out How Corvalin Can Help You Put All The Pieces Together<br>And Get Them Done.</p>
</section>

<section class="people">
  <div class="tile teal" style="left:17px;top:0;width:203px;height:35px" role="img" aria-label="Team member portrait"></div>
  <div class="tile pink" style="left:17px;top:58px;width:203px;height:305px" role="img" aria-label="Portrait of a smiling woman in a white sweater"></div>
  <div class="tile pink" style="left:17px;top:385px;width:203px;height:200px" role="img" aria-label="Portrait of a man in a striped shirt"></div>
  <div class="tile pink" style="left:17px;top:605px;width:203px;height:145px" role="img" aria-label="Portrait of a woman with glasses"></div>
  <div class="tile blue-t" style="left:237px;top:0;width:250px;height:150px" role="img" aria-label="Portrait of a person in a blue sweater"></div>
  <div class="tile grey" style="left:237px;top:165px;width:250px;height:210px" role="img" aria-label="Portrait of a man in an orange sweater"></div>
  <div class="tile pink" style="left:237px;top:385px;width:250px;height:335px" role="img" aria-label="Portrait of a smiling woman with hand on chin"></div>
  <div class="tile grey" style="left:237px;top:720px;width:250px;height:30px" role="img" aria-label="Team member portrait"></div>

  <div class="sq" style="left:523px;top:236px;width:10px;height:10px;background:var(--yellow)"></div>
  <div class="pixel-deco" style="left:1076px;top:30px;width:122px;height:106px" role="img" aria-label="Decorative cluster of pixel squares"></div>
  <div class="sq" style="left:1032px;top:662px;width:10px;height:10px;background:var(--yellow)"></div>

  <h2>It's The People</h2>
  <p class="copy">The World Has Changed In The Past Twenty Years. The People You Need Might Not All Work For One Company. Our Clients Want The Best Resources, Available Quickly. That's Why, In Addition To Our Team Of Experts, We Partner With:</p>
  <div class="box" style="top:320px;height:93px">A Large Network Of Expert Consultants Who Are The Best At What They Do,</div>
  <div class="box" style="top:425px;height:95px">Service Providers All Over The World To Provide The Resources And Value That Are Right For You, Available 24 X 7.</div>
  <p class="strong">People Are Invariably At The Center Of Our Customer's Success.<br>Find Out How We Can Add Our Experts To Yours.</p>
</section>

<section class="testimonials">
  <h2 class="sec-title" style="top:2575px;font-size:38px">Testimonials</h2>
  <div class="sq" style="left:930px;top:2588px;width:10px;height:10px;background:var(--blue)"></div>

  <div class="testi-col" style="left:125px">
    <div class="t-card"><div class="t-head"><div class="avatar"></div><div><b>Dana Whitlock</b><span>Business Name</span></div></div><p>Lorem Ipsum is simply dummy text of the printing and typesetting industry. Lorem Ipsum has been the industry's standard dummy text ever since the 1500s, when an unknown printer took a galley</p><div class="stars">★★★★★</div></div>
    <div class="t-card"><div class="t-head"><div class="avatar"></div><div><b>Dana Whitlock</b><span>Business Name</span></div></div><p>Lorem Ipsum is simply dummy text of the printing and typesetting industry. Lorem Ipsum has been the industry's standard dummy text ever since the 1500s, when an unknown printer took a galley of type and scrambled it to make a type specimen book. It has survived not only five centuries, but also the leap into electronic typesetting, remaining essentially unchanged.</p><div class="stars">★★★★★</div></div>
  </div>
  <div class="testi-col" style="left:365px">
    <div class="t-card"><div class="t-head"><div class="avatar"></div><div><b>Dana Whitlock</b><span>Business Name</span></div></div><p>Lorem Ipsum is simply dummy text of the printing and typesetting industry. Lorem Ipsum has been the industry's standard dummy text ever since the 1500s, when an unknown printer took a galley of type and scrambled it to make a type specimen book. It has survived not only five centuries, but also the leap into electronic typesetting, remaining essentially unchanged.</p><div class="stars">★★★★★</div></div>
    <div class="t-card"><div class="t-head"><div class="avatar"></div><div><b>Dana Whitlock</b><span>Business Name</span></div></div><p>Lorem Ipsum is simply dummy text of the printing and typesetting industry. Lorem Ipsum has been the industry's standard dummy text ever since the 1500s, when an unknown printer took a galley</p><div class="stars">★★★★★</div></div>
  </div>
  <div class="testi-col" style="left:605px">
    <div class="t-card"><div class="t-head"><div class="avatar"></div><div><b>Dana Whitlock</b><span>Business Name</span></div></div><p>Lorem Ipsum is simply dummy text of the printing and typesetting industry. Lorem Ipsum has been the industry's standard dummy text ever since the 1500s, when an unknown printer took a galley</p><div class="stars">★★★★★</div></div>
    <div class="t-card"><div class="t-head"><div class="avatar"></div><div><b>Dana Whitlock</b><span>Business Name</span></div></div><p>Lorem Ipsum is simply dummy text of the printing and typesetting industry. Lorem Ipsum has been the industry's standard dummy text ever since the 1500s, when an unknown printer took a galley of type and scrambled it to make a type specimen book. It has survived not only five centuries, but also the leap into electronic typesetting, remaining essentially unchanged.</p><div class="stars">★★★★★</div></div>
  </div>
  <div class="testi-col" style="left:845px">
    <div class="t-card"><div class="t-head"><div class="avatar"></div><div><b>Dana Whitlock</b><span>Business Name</span></div></div><p>Lorem Ipsum is simply dummy text of the printing and typesetting industry. Lorem Ipsum has been the industry's standard dummy text ever since the 1500s, when an unknown printer took a galley of type and scrambled it to make a type specimen book. It has survived not only five centuries, but also the leap into electronic typesetting, remaining essentially unchanged.</p><div class="stars">★★★★★</div></div>
    <div class="t-card"><div class="t-head"><div class="avatar"></div><div><b>Dana Whitlock</b><span>Business Name</span></div></div><p>Lorem Ipsum is simply dummy text of the printing and typesetting industry. Lorem Ipsum has been the industry's standard dummy text ever since the 1500s, when an unknown printer took a galley</p><div class="stars">★★★★★</div></div>
  </div>

  <div class="sq" style="left:1093px;top:3160px;width:16px;height:16px;background:var(--sky-2)"></div>
  <div class="pixel-deco" style="left:0;top:3188px;width:64px;height:94px" role="img" aria-label="Decorative cluster of pixel squares"></div>
</section>

<section class="tech">
  <div class="sq" style="left:28px;top:100px;width:14px;height:14px;background:#fff"></div>
  <h2>Technologies</h2>
  <div class="arrow-btn" style="left:125px"><svg width="70" height="46" viewBox="0 0 70 46"><path d="M52 23H18M26 16l-8 7 8 7" stroke="#f5c518" stroke-width="2" fill="none"/></svg></div>
  <div class="arrow-btn" style="left:205px"><svg width="70" height="46" viewBox="0 0 70 46"><path d="M18 23h34M44 16l8 7-8 7" stroke="#f5c518" stroke-width="2" fill="none"/></svg></div>
  <div class="shot" style="left:445px;background:linear-gradient(160deg,#e8ecef,#9aa4ac)" role="img" aria-label="Laptop showing an order processing dashboard"></div>
  <div class="shot" style="left:810px;background:linear-gradient(160deg,#c9d3dc,#5a6570)" role="img" aria-label="Laptop showing sales charts"></div>
  <div class="shot" style="left:1175px;width:25px;background:linear-gradient(160deg,#d8d8d8,#9a9a9a)" role="img" aria-label="Technology image"></div>
  <div class="sq" style="left:434px;top:488px;width:10px;height:10px;background:var(--sky-2)"></div>
  <p class="caption" style="left:523px">Order&nbsp; Processing</p>
  <p class="caption" style="left:889px">Sales Automation</p>
  <div class="sq" style="left:1108px;top:548px;width:12px;height:12px;background:var(--yellow)"></div>
  <div class="pixel-deco" style="left:1116px;top:592px;width:84px;height:62px" role="img" aria-label="Decorative cluster of pixel squares"></div>
</section>

<footer class="footer">
  <div class="f-logo">Corvalin</div>
  <div class="f-item" style="top:186px"><div class="f-icon"><svg width="18" height="18" viewBox="0 0 24 24"><path d="M6.6 10.8a15 15 0 006.6 6.6l2.2-2.2c.3-.3.7-.4 1-.2 1.1.4 2.3.6 3.6.6.6 0 1 .4 1 1V20c0 .6-.4 1-1 1A17 17 0 013 4c0-.6.4-1 1-1h3.5c.6 0 1 .4 1 1 0 1.3.2 2.5.6 3.6.1.3 0 .7-.2 1z" fill="#fff"/></svg></div>(555) 014-2286</div>
  <div class="f-item" style="top:262px"><div class="f-icon"><svg width="18" height="18" viewBox="0 0 24 24"><rect x="3" y="6" width="18" height="12" rx="1" fill="#fff"/><path d="M3 7l9 6 9-6" stroke="#2b2b2b" stroke-width="1.5" fill="none"/></svg></div>info@corvalin.com</div>
  <div class="f-item" style="top:355px"><div class="f-icon"><svg width="18" height="18" viewBox="0 0 24 24"><path d="M12 2a7 7 0 00-7 7c0 5 7 13 7 13s7-8 7-13a7 7 0 00-7-7zm0 9.5A2.5 2.5 0 1112 6a2.5 2.5 0 010 5.5z" fill="#fff"/></svg></div>48 Harborline Plaza Suite<br>210, Eastfield, MN 55990</div>
  <div class="f-col" style="left:517px"><h4>Links</h4><a href="#">Home</a><a href="#">About Us</a><a href="#">Services</a><a href="#">Insights</a><a href="#">Join Us</a></div>
  <div class="f-col" style="left:692px"><h4>Company</h4><a href="#">Community</a><a href="#">Blog</a><a href="#">Forums</a><a href="#">Meetups</a></div>
  <p class="copy-r">© Copyright 2023 Corvalin</p>
  <a class="social" href="#" style="left:908px" aria-label="Social link"></a>
  <a class="social" href="#" style="left:953px" aria-label="Social link"></a>
  <a class="social" href="#" style="left:998px" aria-label="Social link"></a>
  <a class="social" href="#" style="left:1043px" aria-label="Social link"></a>
</footer>

</body>
</html>
```